Manufacturing business needs a website revamp

We are a manufacturing business supplying parts and modules to mid-high end consumer electronics brands from kitchen appliances to powered tools mainly in US/Europe. We want design ideas for a revamp of our website. We're aiming for a look and feel that's sleek, tidy and modern whilst still providing the right balance for content. A smooth and comfortable user experience that directs users to the information they may be looking for and promote our services. Something that incorporates design ideas such as: responsive design, lazy loading, slider banners, responsive layout, dynamic scrolling, liquid layout, full page headers etc... These are just terms bounced around within our team and certainly neither exclusive nor absolutely necessary. This is our current website for reference: https://www.varlumotek.com/ , which we feel is both outdated and doesn't engage visitors.

Attached is our planned new site map (we’re open to additional ideas here). We would like mock ups for each page on the site map. We will subsequently fill out the contents ourselves, but require design directions on e.g. how much text should go at which spot. E.g. for our Automotive page under Industries, we would like a suitable layout to be designed, as well as designated areas for texts. As for assets, please use any of the assets already on our current site or external source. We’ve yet to finalize on our selection of assets so please use the above as placeholders for now. Additionally, we would want a mock up for a pop-up frame to showcase additional technical specifications for some of our product ranges. For example, under the powertools section of our current website, we have additional listings under our product range. Currently they do not have a pop up function, but if we were to create a pop up frame to display detailed specifications, what layout should we use?

Finally, our target audiences are professional representatives from leading consumer brands who may be interested in our services. Our target customers are mid-high end brands. Think, for example, KVR/Harwick for automotive, Frostivane/Trell/Dovarin for consumer electronics/kitchen appliances, and Pelham Grove & Tasker/Brantover for powered tools. Typically it will be their product designers/engineers and supply chain representatives who will visit our website.

Target Market(s)

Professional product engineers/designers from mid-high end consumer electronics brands.

Industry/Entity Type

Manufacturing

Contact Information for Business Card

Attached are back and front of our current name card design. Again, we're open to changes that matches the style of our future website design. A few notes on the business card design:
- Cannot have blue background
- Does not have to be bilingual. I.e. open to single language design on one side and logo on the other

Coding

Coded - Design and coding required

Number of Pages Required

5+ page

Font styles to use
Sans Serif

Colors
3176b5

Requirements
Must have
• Color scheme must be based on the blue from our current website design. We will be keeping our current logo, hence must match that logo.
Nice to have
• Plim (or similar platforms) as demos/final solutions ok.
Should not have
• See brief

```html
<!DOCTYPE html>
<html lang="en">
<head>
<meta charset="utf-8">
<title>Varlumo — Manufacturing Partner</title>
<link rel="stylesheet" href="https://fonts.googleapis.com/css2?family=Poppins:wght@300;400;500;600&display=swap">
<style>
:root{
  --blue:#4399c9;
  --blue-dark:#3176b5;
  --ink:#2b2b2b;
  --muted:#7a7a7a;
  --soft:#f4f5f7;
  --white:#ffffff;
  --line:#e3e3e3;
}
*{box-sizing:border-box;margin:0;padding:0}
html,body{width:1200px;height:4225px;overflow:hidden}
body{font-family:'Poppins',sans-serif;color:var(--ink);background:var(--white)}
.page{position:relative;width:1200px;height:4225px}
.abs{position:absolute}
.section{position:absolute;left:0;width:1200px}
.center{text-align:center}
.title{position:absolute;left:0;width:1200px;text-align:center;font-size:25px;font-weight:500;letter-spacing:.3px;text-transform:uppercase}
.rule{position:absolute;left:579px;width:42px;height:3px;background:var(--ink)}
.btn{position:absolute;background:var(--blue);color:var(--white);font-size:11px;display:flex;align-items:center;justify-content:center}
.btn-white{background:var(--white);color:var(--blue)}
.photo{position:absolute}

/* top bar */
.topbar{top:0;height:39px;background:var(--blue);color:var(--white);font-size:13px}
.topbar .phone{left:148px;top:10px;display:flex;align-items:center;gap:10px}
.topbar .social{right:140px;top:11px;display:flex;gap:10px}
.topbar .social span{width:14px;height:14px;background:var(--white);opacity:.9;border-radius:2px}
.nav{top:39px;height:71px;background:var(--white);box-shadow:0 1px 3px rgba(0,0,0,.05)}
.brand{left:148px;top:16px;display:flex;align-items:center;gap:8px;font-size:24px;font-weight:600;color:var(--ink)}
.brand i{width:30px;height:30px;background:var(--blue);display:block}
.menu{right:142px;top:28px;display:flex;gap:32px;font-size:12px;color:#8a8a8a;text-transform:uppercase}
.menu .active{color:var(--blue)}

/* hero */
.hero{top:110px;height:467px;background:linear-gradient(120deg,#5d8fba 0%,#3d6f9d 45%,#2d5a86 100%)}
.hero h1{position:absolute;left:0;width:1200px;top:125px;text-align:center;color:var(--white);font-size:44px;font-weight:600;line-height:44px}
.hero .btn{left:528px;top:290px;width:144px;height:44px;font-size:16px}

/* industries */
.card-label{position:absolute;background:var(--blue);color:var(--white);font-size:16px;display:flex;align-items:center;justify-content:center;text-align:center;line-height:17px}

/* about */
.about{top:1071px;height:397px;background:var(--blue);color:var(--white)}
.about h2{position:absolute;left:148px;top:100px;font-size:25px;font-weight:500}
.about p{position:absolute;left:148px;top:155px;width:415px;font-size:10px;line-height:17.5px}
.about .btn{left:148px;top:262px;width:77px;height:29px;font-size:10px}

.core{top:1468px;height:461px;background:var(--soft)}
.stats{top:1929px;height:351px;background:linear-gradient(180deg,#4a9dcc,#4599c9)}
.stats h2{position:absolute;left:0;width:1200px;top:66px;text-align:center;color:var(--white);font-size:24px;font-weight:500}
.stats p{position:absolute;left:200px;width:800px;top:128px;text-align:center;color:var(--white);font-size:10px;line-height:17px}
.stat{position:absolute;top:195px;width:200px;text-align:center;color:var(--white)}
.stat b{display:block;font-size:44px;font-weight:400;line-height:50px}
.stat small{font-size:12px}
.divider{position:absolute;top:202px;width:2px;height:76px;background:rgba(255,255,255,.85)}

.news{top:2280px;height:626px;background:var(--soft)}
.news-card{position:absolute;top:172px;width:292px;height:351px;background:var(--white);text-align:center}
.news-card h3{position:absolute;top:191px;width:100%;font-size:16px;font-weight:500}
.news-card p{position:absolute;top:219px;left:36px;width:220px;font-size:9.5px;line-height:15px;color:var(--muted)}
.news-card .btn{left:109px;top:297px;width:75px;height:24px;font-size:9.5px}

.partners{top:2906px;height:317px;background:var(--white)}
.partner{position:absolute;top:172px;height:40px;background:#c9ccd1;border-radius:4px}

.quote{top:3223px;height:370px;background:linear-gradient(180deg,#4c9ecc,#4397c7);color:var(--white)}
.quote .mark{position:absolute;left:0;width:1200px;top:52px;text-align:center;font-size:60px;font-weight:600;line-height:60px}
.quote p{position:absolute;left:300px;width:600px;top:122px;text-align:center;font-size:12px;line-height:19px}
.quote .avatar{position:absolute;left:567px;top:195px;width:66px;height:66px;border-radius:50%;background:#dfe7ef;border:3px solid var(--white)}
.quote .name{position:absolute;left:0;width:1200px;top:266px;text-align:center;font-size:14px;font-weight:500}
.quote .date{position:absolute;left:0;width:1200px;top:286px;text-align:center;font-size:10px}

.newsletter{top:3593px;height:369px;background:var(--white)}
.newsletter p{position:absolute;left:255px;width:690px;top:158px;text-align:center;font-size:12px;line-height:19px;color:var(--muted)}
.newsletter .field{position:absolute;left:356px;top:227px;width:341px;height:41px;background:var(--soft);font-size:10px;color:#b8b8b8;padding:14px 0 0 22px}
.newsletter .btn{left:697px;top:227px;width:148px;height:41px;font-size:13px;font-weight:500}

.footer{top:3962px;height:263px;background:var(--blue);color:var(--white)}
.footer .logo{position:absolute;left:148px;top:70px;display:flex;align-items:center;gap:12px;font-size:38px;font-weight:500}
.footer .logo i{width:46px;height:46px;background:var(--white);display:block}
.footer .socials{position:absolute;left:148px;top:163px;display:flex;gap:12px}
.footer .socials span{width:25px;height:25px;background:var(--white);border-radius:2px}
.fcol{position:absolute;top:67px;font-size:10px}
.fcol h4{font-size:16px;font-weight:400;margin-bottom:16px}
.fcol li{list-style:none;height:28px}
.fcol .c{display:flex;gap:8px;width:180px;line-height:14px;height:auto;margin-bottom:12px}
.copy{position:absolute;left:0;width:1200px;top:223px;text-align:center;font-size:10px}
</style>
</head>
<body>
<div class="page">

  <header>
    <div class="section topbar">
      <div class="abs phone">
        <svg width="14" height="14" viewBox="0 0 24 24" fill="#fff"><path d="M6.6 10.8a15 15 0 0 0 6.6 6.6l2.2-2.2c.3-.3.7-.4 1-.2 1.1.4 2.3.6 3.6.6.6 0 1 .4 1 1V20c0 .6-.4 1-1 1A17 17 0 0 1 3 4c0-.6.4-1 1-1h3.5c.6 0 1 .4 1 1 0 1.3.2 2.5.6 3.6.1.3 0 .7-.2 1z"/></svg>
        <span>(86) 0755-41908362</span>
      </div>
      <div class="abs social"><span></span><span></span><span></span><span></span></div>
    </div>
    <nav class="section nav">
      <div class="abs brand"><i></i>Varlumo</div>
      <div class="abs menu">
        <span class="active">Home</span><span>About</span><span>Industries ⌄</span><span>Core Competencies ⌄</span><span>News</span><span>Contact</span>
      </div>
    </nav>
  </header>

  <section class="section hero" role="img" aria-label="Factory automation robot arm with blue technology overlay">
    <h1>Join the Modern Electric family!<br>Click Here To See Available<br>Positions.</h1>
    <div class="btn">Contact Us</div>
  </section>

  <section class="section" style="top:577px;height:494px">
    <h2 class="title" style="top:95px">Industries</h2>
    <div class="rule" style="top:139px"></div>
    <div class="photo" role="img" aria-label="Silver sedan in motion" style="left:148px;top:174px;width:292px;height:161px;background:linear-gradient(135deg,#e6e9ec,#9aa3ab)"></div>
    <div class="card-label" style="left:148px;top:335px;width:292px;height:57px">Automotive</div>
    <div class="photo" role="img" aria-label="Kitchen appliances on a counter" style="left:457px;top:174px;width:292px;height:161px;background:linear-gradient(135deg,#efeeec,#8d8a86)"></div>
    <div class="card-label" style="left:457px;top:335px;width:292px;height:57px">Home Appliances</div>
    <div class="photo" role="img" aria-label="Angle grinder throwing sparks" style="left:767px;top:174px;width:292px;height:161px;background:linear-gradient(135deg,#3a3a3c,#c58a3b)"></div>
    <div class="card-label" style="left:767px;top:335px;width:292px;height:57px">Power Tools</div>
  </section>

  <section class="section about">
    <h2>ABOUT US</h2>
    <p>Lorem Ipsum is simply dummy text of the printing and typesetting industry. Lorem Ipsum has been the industry's standard dummy text ever since the 1500s, when an unknown printer took a galley of type and scrambled it to make a type specimen book. It has survived not only five centuries, but also the leap into electronic typesetting, remaining essentially unchanged.</p>
    <div class="btn btn-white">Read More</div>
    <div class="photo" role="img" aria-label="Industrial robots on an assembly line" style="left:612px;top:66px;width:447px;height:265px;background:linear-gradient(135deg,#d9dde2,#6e7784 60%,#b8623a)"></div>
  </section>

  <section class="section core">
    <h2 class="title" style="top:96px">Core Competencies</h2>
    <div class="rule" style="top:140px"></div>
    <div class="photo" role="img" aria-label="Team holding awards" style="left:148px;top:172px;width:213px;height:126px;background:linear-gradient(135deg,#4a4140,#a0928a)"></div>
    <div class="card-label" style="left:148px;top:298px;width:213px;height:61px">Awards &amp; Honors</div>
    <div class="photo" role="img" aria-label="Engineers at a workstation" style="left:382px;top:172px;width:213px;height:126px;background:linear-gradient(135deg,#dbe4ea,#6f8fa8)"></div>
    <div class="card-label" style="left:382px;top:298px;width:213px;height:61px">Research and<br>Development</div>
    <div class="photo" role="img" aria-label="Manufacturing floor in blue tint" style="left:610px;top:172px;width:213px;height:187px;background:linear-gradient(135deg,#6aa8d2,#4a8fc0)"></div>
    <div class="abs center" style="left:610px;top:199px;width:213px;color:#fff">
      <div style="font-size:16px;line-height:17px">Manufacturing<br>Capabilities</div>
      <div style="font-size:9.5px;line-height:12px;margin:9px 18px 0">Efficient and flexible, while maintaining the best Quality and Consistency.</div>
    </div>
    <div class="btn btn-white" style="left:679px;top:297px;width:77px;height:28px;font-size:9.5px">Read More</div>
    <div class="photo" role="img" aria-label="Technician inspecting parts" style="left:845px;top:172px;width:213px;height:126px;background:linear-gradient(135deg,#cfd6dd,#6b7785)"></div>
    <div class="card-label" style="left:845px;top:298px;width:213px;height:61px">Quality<br>Management</div>
  </section>

  <section class="section stats">
    <h2>20 YEARS OF EXPERIENCE IN VARIOUS CASES</h2>
    <p>Lorem Ipsum is simply dummy text of the printing and typesetting industry. Lorem Ipsum has been the industry's standard dummy text ever since the 1500s, when an unknown printer took a galley of type and scrambled it to make a type specimen book.</p>
    <div class="stat" style="left:195px"><b>140K</b><small>Projects</small></div>
    <div class="divider" style="left:447px"></div>
    <div class="stat" style="left:500px"><b>84</b><small>Advisor</small></div>
    <div class="divider" style="left:755px"></div>
    <div class="stat" style="left:813px"><b>95%</b><small>Satisfaction Rate</small></div>
  </section>

  <section class="section news">
    <h2 class="title" style="top:94px">Latest News</h2>
    <div class="rule" style="top:138px"></div>
    <article class="news-card" style="left:148px">
      <div class="photo" role="img" aria-label="Desk with notebook and coffee" style="left:0;top:0;width:292px;height:161px;background:linear-gradient(135deg,#3d2f28,#a58a72)"></div>
      <h3>Tax Planning &amp; Preparation</h3>
      <p>Lorem Ipsum is simply dummy text of the printing and typesetting industry. Lorem Ipsum has been the industry's standard dummy text ever since the 1500s,</p>
      <div class="btn">Read More</div>
    </article>
    <article class="news-card" style="left:457px">
      <div class="photo" role="img" aria-label="Laptop beside printed charts" style="left:0;top:0;width:292px;height:161px;background:linear-gradient(135deg,#6b6d70,#eceae6)"></div>
      <h3>Construction Investment plan</h3>
      <p>Lorem Ipsum is simply dummy text of the printing and typesetting industry. Lorem Ipsum has been the industry's standard dummy text ever since the 1500s,</p>
      <div class="btn">Read More</div>
    </article>
    <article class="news-card" style="left:767px">
      <div class="photo" role="img" aria-label="Desktop monitor showing a dashboard" style="left:0;top:0;width:292px;height:161px;background:linear-gradient(135deg,#f2f2f2,#c9ccd0)"></div>
      <h3>Small Business Accounting</h3>
      <p>Lorem Ipsum is simply dummy text of the printing and typesetting industry. Lorem Ipsum has been the industry's standard dummy text ever since the 1500s,</p>
      <div class="btn">Read More</div>
    </article>
  </section>

  <section class="section partners">
    <h2 class="title" style="top:95px">Our Partners</h2>
    <div class="rule" style="top:139px"></div>
    <div class="partner" style="left:170px;width:170px"></div>
    <div class="partner" style="left:413px;width:148px"></div>
    <div class="partner" style="left:650px;width:138px"></div>
    <div class="partner" style="left:884px;width:136px"></div>
  </section>

  <section class="section quote">
    <div class="mark">&ldquo;</div>
    <svg class="abs" style="left:204px;top:147px" width="16" height="26" viewBox="0 0 16 26"><path d="M13 2 3 13l10 11" stroke="#fff" stroke-width="2" fill="none"/></svg>
    <svg class="abs" style="left:984px;top:147px" width="16" height="26" viewBox="0 0 16 26"><path d="M3 2l10 11L3 24" stroke="#fff" stroke-width="2" fill="none"/></svg>
    <p>Lorem Ipsum is simply dummy text of the printing and typesetting industry. Lorem Ipsum has been the industry's standard dummy text ever since the 1500s, when an unknown printer took a galley of type and scrambled it to make a type specimen book.</p>
    <div class="avatar" role="img" aria-label="Client portrait"></div>
    <div class="name">John Doe</div>
    <div class="date">14 Sep, 2020</div>
  </section>

  <section class="section newsletter">
    <h2 class="title" style="top:93px">Join Our Newsletter</h2>
    <div class="rule" style="top:135px"></div>
    <p>Lorem Ipsum is simply dummy text of the printing and typesetting industry. Lorem Ipsum has been the industry's standard dummy text ever since the 1500s,</p>
    <div class="field">Enter your Email</div>
    <div class="btn">Subscribe</div>
  </section>

  <footer class="section footer">
    <div class="logo"><i></i>Varlumo</div>
    <div class="socials"><span></span><span></span><span></span><span></span></div>
    <div class="fcol" style="left:407px">
      <h4>INFORMATION</h4>
      <ul><li>Help &amp; FAQs</li><li>Advance Search</li><li>Gift Cards</li><li>Shop By Brands</li></ul>
    </div>
    <div class="fcol" style="left:640px">
      <h4>ACCOUNT</h4>
      <ul><li>Preference</li><li>Order history</li><li>Cart Page</li><li>Sign In</li></ul>
    </div>
    <div class="fcol" style="left:874px">
      <h4>CONTACT</h4>
      <ul>
        <li class="c"><svg width="9" height="12" viewBox="0 0 10 14"><path d="M5 0a5 5 0 0 0-5 5c0 4 5 9 5 9s5-5 5-9a5 5 0 0 0-5-5zm0 7a2 2 0 1 1 0-4 2 2 0 0 1 0 4z" fill="#fff"/></svg><span>No. 14 Lakeside Works Park, Qingxi District, Harbourline City, PRC</span></li>
        <li class="c"><svg width="10" height="10" viewBox="0 0 24 24" fill="#fff"><path d="M6.6 10.8a15 15 0 0 0 6.6 6.6l2.2-2.2c.3-.3.7-.4 1-.2 1.1.4 2.3.6 3.6.6.6 0 1 .4 1 1V20c0 .6-.4 1-1 1A17 17 0 0 1 3 4c0-.6.4-1 1-1h3.5c.6 0 1 .4 1 1 0 1.3.2 2.5.6 3.6.1.3 0 .7-.2 1z"/></svg><span>(86) 0755-41908362</span></li>
        <li class="c"><svg width="10" height="8" viewBox="0 0 12 9"><rect width="12" height="9" fill="#fff"/><path d="M0 0l6 5 6-5" stroke="#4399c9" fill="none"/></svg><span>info@varlumotek.com</span></li>
      </ul>
    </div>
    <div class="copy">Copyright 2020-2030.Reserved all rights</div>
  </footer>

</div>
</body>
</html>
```